Talvora Companies Business Card Design

We need a new business card for our Private Equity Real Estate Development firm, “Talvora” and our EB-5 regional center “Mossgate Regional Center” on one card. We prefer a design that is simple, elegant, and represents the luxury products we design and build as well as the financial security and stability our successful history has produced. We are an industry leader in our field and 3rd generation family business that has evolved into an institutional quality investment platform. Considered design size is standard business card dimensions (3.5 x 2 inches with an additional 1/8 inch space for design elements or backgrounds that extend beyond the finished size of your piece.

Target Market(s)

• High net worth individuals
• Highly skilled technical workers and physicians in the US seeking investment-based immigration opportunities
• Sophisticated private equity investors
• Intermediary partners include domestic attorneys and investment brokers, as well as international agent networks
• US real estate developers

Industry/Entity Type

Finance

Contact Information for Business Card

(Providing placeholder info for personal information, please design for longer character spaces, longer names and addresses etc..)
• Logo for Talvora
• Logo for Mossgate Regional Center
• Full name: Dermot Talvora
• Job title: CEO
• Email address: dtalvora@talvoracompanies.com
• Cell phone number: +1.555.314.2786
• Office number +1.555.862.4071
• Office address: Quillfield Park 7, 4817 Vista Loma, San Ramon, CA.
• Website: www.talvoracompanies.com

Font styles to use
Serif
Sans Serif

Colors
ec1f27
ffffff
000000

Requirements
Must have
• • Logo for Talvora
• • Logo for Mossgate Regional Center
• - Use rounded corners
• (See .ai file included for logos)
Nice to have
• • Simple, elegant design
• • Aesthetically compatible with our website design (www.talvoracompanies.com)
• • Color palette including but not limited to white, black, and red (as per logos)
Should not have
• - Not too much red color
• - Do not stack both logos on top of each other

```html
<!DOCTYPE html>
<html lang="en">
<head>
<meta charset="utf-8">
<title>Talvora Companies Business Card</title>
<link rel="stylesheet" href="https://fonts.googleapis.com/css2?family=Cinzel:wght@500;600&family=Roboto:wght@400&display=swap">
<style>
  :root {
    --backdrop: #26272a;
    --paper: #f4f4f4;
    --ink: #454545;
    --black: #111111;
    --brand-red: #9c1a30;
    --card-dark-top: #1b1c1e;
    --card-dark-bottom: #2b2c2f;
    --white: #ffffff;
  }
  * { box-sizing: border-box; margin: 0; padding: 0; }
  html, body { width: 1200px; height: 960px; overflow: hidden; }
  body { background: var(--backdrop); position: relative; font-family: 'Roboto', Arial, sans-serif; }

  .card { position: absolute; width: 600px; height: 343px; border-radius: 6px; }

  .card-front { left: 314px; top: 113px; background: var(--paper); }
  .center-name {
    position: absolute; left: 44px; top: 60px;
    font-family: 'Cinzel', Georgia, serif; font-weight: 600;
    font-size: 21px; letter-spacing: 0.5px; color: var(--brand-red);
  }
  .contact-list { position: absolute; left: 50px; top: 156px; list-style: none; }
  .contact-item {
    display: flex; align-items: flex-start; gap: 9px;
    font-size: 14.5px; line-height: 19px; color: var(--ink);
  }
  .contact-item.address { margin-bottom: 12px; line-height: 18px; }
  .contact-icon { width: 14px; height: 14px; flex: none; margin-top: 2px; fill: var(--brand-red); }
  .person { position: absolute; right: 38px; top: 200px; text-align: right; }
  .person-name {
    font-family: 'Cinzel', Georgia, serif; font-weight: 500;
    font-size: 24px; color: var(--brand-red); line-height: 1;
  }
  .person-title {
    margin-top: 7px; font-size: 13px; letter-spacing: 3px;
    color: var(--black); margin-right: -3px;
  }

  .card-back {
    left: 312px; top: 472px; height: 342px;
    background: linear-gradient(160deg, var(--card-dark-top), var(--card-dark-bottom));
    display: flex; flex-direction: column; align-items: center; justify-content: center;
  }
  .firm-name {
    font-family: 'Cinzel', Georgia, serif; font-weight: 600;
    font-size: 44px; color: var(--white); line-height: 1; letter-spacing: 1px;
  }
  .firm-division {
    margin-top: 10px; font-family: 'Cinzel', Georgia, serif; font-weight: 600;
    font-size: 15px; letter-spacing: 5px; color: var(--white);
  }
</style>
</head>
<body>
  <section class="card card-front">
    <div class="center-name">MOSSGATE REGIONAL CENTER</div>

    <ul class="contact-list">
      <li class="contact-item address">
        <svg class="contact-icon" viewBox="0 0 14 14"><path d="M7 0a5 5 0 0 0-5 5c0 3.6 5 9 5 9s5-5.4 5-9a5 5 0 0 0-5-5zm0 7a2 2 0 1 1 0-4 2 2 0 0 1 0 4z"/></svg>
        <span>Quillfield Park 7<br>4817 Vista Loma<br>San Ramon, CA.</span>
      </li>
      <li class="contact-item">
        <svg class="contact-icon" viewBox="0 0 14 14"><path d="M3 0l2.5 3-1.5 2c.8 1.8 2.2 3.2 4 4l2-1.5 3 2.5-1.5 2.5C6 13 1 8 .5 1.5z"/></svg>
        <span>+1.555.862.4071</span>
      </li>
      <li class="contact-item">
        <svg class="contact-icon" viewBox="0 0 14 14"><path d="M3 0h8v14H3zm1.5 1.5v9h5v-9zM6 11.5v1h2v-1z"/></svg>
        <span>+1.555.314.2786</span>
      </li>
      <li class="contact-item">
        <svg class="contact-icon" viewBox="0 0 14 14"><path d="M0 3h14v1L7 8 0 4zm0 2.5l7 4 7-4V11H0z"/></svg>
        <span>dtalvora@talvoracompanies.com</span>
      </li>
      <li class="contact-item">
        <svg class="contact-icon" viewBox="0 0 14 14"><circle cx="7" cy="7" r="6.5"/><path d="M4 4c1 0 2 1 1.5 2S3 7 4 9M9 2.5c-.5 1.5 1 2 2 2.5M8 12c0-2 2-2 2.5-3.5" stroke="#f4f4f4" stroke-width="1.2" fill="none"/></svg>
        <span>www.talvoracompanies.com</span>
      </li>
    </ul>

    <div class="person">
      <div class="person-name">DERMOT TALVORA</div>
      <div class="person-title">CEO</div>
    </div>
  </section>

  <section class="card card-back">
    <div class="firm-name">TALVORA</div>
    <div class="firm-division">CAPITAL</div>
  </section>
</body>
</html>
```